Qb Panes

We need a website design for a company based in Texas that specializes in doors and and windows.
Qb Pane is a leading window manufacturer of aluminum and vinyl windows, both serving the replacement and new construction markets. Qb Pane Inc. was created over 25 years ago when two existing window manufacturers with excellent reputations in their fields - merged. Qb Pane offers a complete line conforming to the needs of residential and commercial window markets.
The final design should be something that communicates professionalism and features they're key value propositions.
Example websites we like:
http://layouts.pebblecraft.example/zx/satchel/
http://layouts.pebblecraft.example/zx/splashyard/
http://layouts.pebblecraft.example/zx/rebuildr2/
This design should format the existing content to be more visually organized, improve the fonts to clearer and more readable, and make it easier for users to find services.
Brand guide is attached
Website images can be found here: https://docs.vaultcrate.example/7kRTmwQzLpXeBd
Target Market(s)
Windows
Number of Pages Required
1 page
Look and feel
Each slider illustrates characteristics of the customer's brand and the style your logo design should communicate.

```html
<!DOCTYPE html>
<html lang="en">
<head>
<meta charset="utf-8">
<title>Qb Pane</title>
<link href="https://fonts.googleapis.com/css2?family=Oswald:wght@400;500&family=Roboto:wght@400;500;700&display=swap" rel="stylesheet">
<style>
:root{
  --crimson:#9d1a3b;
  --gold:#e4b12a;
  --ink:#222;
  --muted:#7a7a7a;
  --night:#050505;
  --white:#fff;
}
*{margin:0;padding:0;box-sizing:border-box}
html,body{width:1200px;height:3614px;overflow:hidden}
body{position:relative;background:var(--white);font-family:Roboto,sans-serif;color:var(--ink)}
.abs{position:absolute}
.heading{font-family:Oswald,sans-serif;font-weight:400;text-transform:uppercase;text-align:center;left:0;width:1200px}
.btn{position:absolute;background:var(--crimson);color:var(--white);font:700 12px Roboto,sans-serif;text-transform:uppercase;display:flex;align-items:center;justify-content:center;letter-spacing:.3px}
.media{position:absolute}

/* header */
.site-header{left:0;top:0;width:1200px;height:87px;background:var(--white)}
.brand{left:72px;top:26px;font:400 38px Roboto,sans-serif;color:var(--crimson);line-height:1}
.nav{right:72px;top:34px;display:flex;gap:36px;list-style:none}
.nav li{font:400 14px Roboto,sans-serif;text-transform:uppercase;color:var(--ink);position:relative}
.nav li.active::after{content:"";position:absolute;left:0;right:0;bottom:-8px;height:3px;background:var(--crimson)}

/* hero */
.hero{left:0;top:87px;width:1200px;height:501px;background:linear-gradient(90deg,#d9d4cd 0%,#ece9e4 40%,#f4f3f1 100%)}
.hero-photo{left:0;top:0;width:700px;height:501px;background:linear-gradient(120deg,#b7a898,#e2ddd6 60%,#efedea)}
.hero-title{left:670px;top:140px;font:400 62px Oswald,sans-serif;color:var(--crimson);letter-spacing:1px}
.hero-call{left:670px;top:230px;width:400px;text-align:center;font:400 32px Oswald,sans-serif;color:var(--ink);line-height:1.35}
.hero-dots{left:1088px;top:472px;display:flex;gap:5px}
.hero-dots span{width:10px;height:10px;background:var(--crimson)}
.hero-dots span:first-child{background:#777}
.hero-rule{left:0;top:588px;width:1200px;height:8px;background:#8d8d8d}

/* about */
.about-title{left:72px;top:640px;font:400 40px Oswald,sans-serif;text-transform:uppercase}
.about-text{left:72px;top:706px;width:240px;font:400 13px/24px Roboto,sans-serif}
.about-photo{top:648px;width:244px;height:405px;box-shadow:3px 4px 6px rgba(0,0,0,.35)}

/* services */
.services{left:0;top:1111px;width:1200px;height:241px;background:var(--crimson)}
.services .heading{top:50px;color:var(--white);font-size:34px}
.service{top:127px;display:flex;align-items:center;gap:16px;color:var(--white);font:700 15px/22px Roboto,sans-serif}
.service-icon{width:58px;height:58px;border-radius:50%;background:var(--gold);display:flex;align-items:center;justify-content:center}

/* style gallery */
.style-title{top:1400px;font-size:34px;color:#333}
.tab{top:1466px;height:41px;display:flex;align-items:center;justify-content:center;font:400 21px Roboto,sans-serif;text-transform:uppercase;letter-spacing:1px}
.tab.on{left:431px;width:150px;background:var(--gold);color:var(--white)}
.tab.off{left:619px;color:#555}
.tile{position:absolute}

/* testimonial */
.testimonial{left:0;top:2330px;width:1200px;height:473px;background:var(--crimson);color:var(--white)}
.testimonial .heading{top:55px;font-size:32px;font-weight:500}
.avatar{left:547px;top:117px;width:106px;height:106px;border-radius:50%;background:linear-gradient(#d9c6b6,#8e7c6e);border:4px solid var(--white)}
.quote-badge{left:636px;top:120px;width:40px;height:40px;border-radius:50%;background:var(--white);color:var(--crimson);font:700 34px/52px Georgia,serif;text-align:center}
.arrow{top:254px;width:32px;height:34px;display:flex;align-items:center;justify-content:center}
.quote-text{left:241px;top:264px;width:718px;text-align:center;font:400 13px/26px Roboto,sans-serif}
.quote-rule{left:564px;top:355px;width:72px;height:2px;background:var(--white)}
.quote-name{left:0;width:1200px;top:374px;text-align:center;font:700 12px Roboto,sans-serif}
.quote-role{left:0;width:1200px;top:396px;text-align:center;font:400 13px Roboto,sans-serif}

/* news */
.news-title{top:2852px;font-size:34px;color:#333}
.news-card{top:2923px;width:333px}
.news-img{position:relative;height:157px}
.news-date{position:absolute;left:0;top:0;background:var(--gold);color:var(--white);font:400 12px Roboto,sans-serif;padding:6px 10px}
.news-card h3{margin:22px 10px 0;font:700 15px Roboto,sans-serif}
.news-card p{margin:10px 10px 0;font:400 12px/24px Roboto,sans-serif;color:var(--muted)}

/* footer */
.site-footer{left:0;top:3319px;width:1200px;height:295px;background:var(--night);color:var(--white)}
.footer-brand{left:72px;top:98px;font:400 40px Roboto,sans-serif;color:var(--white)}
.copyright{left:72px;top:156px;font:400 13px Roboto,sans-serif}
.footer-head{font:400 14px Roboto,sans-serif;text-transform:uppercase;letter-spacing:.5px}
.footer-head::after{content:"";display:block;width:34px;height:2px;background:var(--gold);margin-top:8px}
.contact-list{left:583px;top:48px;list-style:none}
.contact-list li{display:flex;gap:14px;font:400 12px/20px Roboto,sans-serif;margin-top:10px}
.contact-list svg{flex:none;margin-top:3px}
.links{left:1024px;top:44px;list-style:none}
.links li{font:400 13px Roboto,sans-serif;text-transform:uppercase;height:31px}
</style>
</head>
<body>

<header class="abs site-header">
  <div class="abs brand">Qb Pane</div>
  <ul class="abs nav">
    <li class="active">Home</li><li>About Us</li><li>Services</li><li>News</li><li>Testmonial</li><li>Contact Us</li>
  </ul>
</header>

<section class="abs hero">
  <div class="abs hero-photo" role="img" aria-label="Smiling senior couple embracing in a bright living room"></div>
  <h1 class="abs hero-title">LOREM IPSUM IS</h1>
  <p class="abs hero-call">NEED HELP? CALL US<br>+00 -5550 -1842</p>
  <div class="abs hero-dots"><span></span><span></span><span></span></div>
</section>
<div class="abs hero-rule"></div>

<section class="about">
  <h2 class="abs about-title">About Us</h2>
  <p class="abs about-text">Lorem Ipsum is simply dummy text of the printing and typesetting industry. Lorem Ipsum has been the industry's standard dummy text ever since the 1500s, when an unknown printer took a galley of type and scrambled it to make a</p>
  <div class="btn" style="left:72px;top:872px;width:108px;height:29px">Read More</div>
  <div class="media about-photo" style="left:345px;background:linear-gradient(#8fb0cf 0%,#5a5d63 45%,#4f7a3a 80%,#6d9c45 100%)" role="img" aria-label="Modern dark grey house with a green lawn"></div>
  <div class="media about-photo" style="left:615px;background:linear-gradient(#f4f2ee 0%,#d9e6cf 40%,#7aa25a 75%,#e8e4da 100%)" role="img" aria-label="White French doors opening to a garden with a white sofa"></div>
  <div class="media about-photo" style="left:885px;background:linear-gradient(#6a5848 0%,#b8cfa3 30%,#6f9a4e 65%,#3d3a36 100%)" role="img" aria-label="Sunroom with large windows, flowers and a striped chair"></div>
</section>

<section class="abs services">
  <h2 class="abs heading">Our Services</h2>
  <div class="abs service" style="left:75px">
    <span class="service-icon"><svg width="30" height="30" viewBox="0 0 30 30" fill="none" stroke="#9d1a3b" stroke-width="2"><rect x="4" y="6" width="22" height="18"/><line x1="4" y1="12" x2="26" y2="12"/><line x1="4" y1="18" x2="26" y2="18"/></svg></span>
    <span>Lorem Ipsum is simply<br>dummy text of the</span>
  </div>
  <div class="abs service" style="left:347px">
    <span class="service-icon"><svg width="30" height="30" viewBox="0 0 30 30" fill="none" stroke="#9d1a3b" stroke-width="2"><rect x="6" y="4" width="18" height="22" rx="2"/><rect x="10" y="8" width="10" height="14"/></svg></span>
    <span>Lorem Ipsum is simply<br>dummy text of the</span>
  </div>
  <div class="abs service" style="left:617px">
    <span class="service-icon"><svg width="30" height="30" viewBox="0 0 30 30" fill="none" stroke="#9d1a3b" stroke-width="2"><path d="M6 26V13a9 9 0 0 1 18 0v13z"/><line x1="15" y1="4" x2="15" y2="26"/><line x1="6" y1="16" x2="24" y2="16"/></svg></span>
    <span>Lorem Ipsum is simply<br>dummy text of the</span>
  </div>
  <div class="abs service" style="left:889px">
    <span class="service-icon"><svg width="30" height="30" viewBox="0 0 30 30" fill="none" stroke="#9d1a3b" stroke-width="2"><rect x="5" y="5" width="20" height="20"/><path d="M5 5l20 20M25 5L5 25"/></svg></span>
    <span>Lorem Ipsum is simply<br>dummy text of the</span>
  </div>
</section>

<section class="styles">
  <h2 class="abs heading style-title">Choose Your Style</h2>
  <div class="abs tab on">Residential</div>
  <div class="abs tab off">Commercial</div>
  <div class="tile" style="left:72px;top:1540px;width:335px;height:255px;background:linear-gradient(135deg,#4a4744,#5d5a57 50%,#3d3b39)" role="img" aria-label="Kitchen with dark cabinets and bright window, dimmed on hover">
    <svg class="abs" style="left:152px;top:112px" width="32" height="32" viewBox="0 0 32 32" fill="none" stroke="#fff" stroke-width="3"><circle cx="13" cy="13" r="9"/><line x1="20" y1="20" x2="29" y2="29"/></svg>
  </div>
  <div class="tile" style="left:72px;top:1822px;width:335px;height:388px;background:linear-gradient(#eae7e2,#c9c3b9 45%,#7a5134 100%)" role="img" aria-label="Open kitchen with white island and wooden floor"></div>
  <div class="tile" style="left:434px;top:1540px;width:335px;height:388px;background:linear-gradient(#c88f4d,#9dbb7a 35%,#d8b98c 70%,#e9e2d4)" role="img" aria-label="Vaulted wood ceiling kitchen with tall windows"></div>
  <div class="tile" style="left:434px;top:1954px;width:335px;height:256px;background:linear-gradient(#f3f1ec,#cfe0c0 45%,#e8e3d8 80%,#b08a5d)" role="img" aria-label="Living room with French doors and white sofa"></div>
  <div class="tile" style="left:795px;top:1540px;width:330px;height:255px;background:linear-gradient(90deg,#ece8e1,#c88a4a 45%,#e5e1da)" role="img" aria-label="Kitchen corner with wood cabinets and window"></div>
  <div class="tile" style="left:795px;top:1822px;width:330px;height:388px;background:linear-gradient(#e8dcc1,#f1ede3 40%,#b9c9a5 60%,#e6dcc4)" role="img" aria-label="Cream kitchen with window above the sink"></div>
  <div class="btn" style="left:528px;top:2239px;width:144px;height:29px">All Collections</div>
</section>

<section class="abs testimonial">
  <h2 class="abs heading">Testimonial</h2>
  <div class="abs avatar" role="img" aria-label="Customer portrait"></div>
  <div class="abs quote-badge">“</div>
  <div class="abs arrow" style="left:72px;background:var(--gold)"><svg width="10" height="14" viewBox="0 0 10 14"><path d="M8 1L2 7l6 6" fill="none" stroke="#9d1a3b" stroke-width="2.5"/></svg></div>
  <div class="abs arrow" style="left:1097px;background:#8d8d8d"><svg width="10" height="14" viewBox="0 0 10 14"><path d="M2 1l6 6-6 6" fill="none" stroke="#fff" stroke-width="2.5"/></svg></div>
  <p class="abs quote-text">Lorem Ipsum is simply dummy text of the printing and typesetting industry. Lorem Ipsum has been the industry's standard dummy text ever since the 1500s, when an unknown printer took a galley of type and scrambled it to make a type specimen book. It has survived not only five centuries, but also the leap into.</p>
  <div class="abs quote-rule"></div>
  <div class="abs quote-name">JOHN DOE</div>
  <div class="abs quote-role">Lorem Ipsum is simply</div>
</section>

<section class="news">
  <h2 class="abs heading news-title">News</h2>
  <article class="abs news-card" style="left:72px">
    <div class="news-img" role="img" aria-label="White kitchen with stainless fridge" style="background:linear-gradient(90deg,#9a9c9e,#e6e4df 50%,#c9c4ba)"><span class="news-date">21 February, 2018</span></div>
    <h3>Lorem Ipsum is simply dummy text</h3>
    <p>Lorem Ipsum is simply dummy text of the printing and typesetting industry. Lorem Ipsum has been the industry's standard dummy text ever since</p>
  </article>
  <article class="abs news-card" style="left:434px">
    <div class="news-img" role="img" aria-label="Wood kitchen with panoramic sea view windows" style="background:linear-gradient(#6e4a2e,#8ab3c9 40%,#9b6a3f 75%,#5a3a24)"><span class="news-date">21 February, 2018</span></div>
    <h3>Lorem Ipsum is simply dummy text</h3>
    <p>Lorem Ipsum is simply dummy text of the printing and typesetting industry. Lorem Ipsum has been the industry's standard dummy text ever since</p>
  </article>
  <article class="abs news-card" style="left:795px">
    <div class="news-img" role="img" aria-label="Cream kitchen sink beneath garden window" style="background:linear-gradient(#dcc8a4,#9fbf7a 40%,#e7dcc6 70%,#b69468)"><span class="news-date">21 February, 2018</span></div>
    <h3>Lorem Ipsum is simply dummy text</h3>
    <p>Lorem Ipsum is simply dummy text of the printing and typesetting industry. Lorem Ipsum has been the industry's standard dummy text ever since</p>
  </article>
  <div class="btn" style="left:547px;top:3227px;width:106px;height:27px">View More</div>
</section>

<footer class="abs site-footer">
  <div class="abs footer-brand">Qb Pane</div>
  <div class="abs copyright">Copyright © 2018 &nbsp;|&nbsp; All Rights Reserved.</div>
  <div class="abs" style="left:583px;top:50px"><div class="footer-head">Contact Us</div></div>
  <ul class="abs contact-list" style="top:88px">
    <li><svg width="12" height="16" viewBox="0 0 12 16"><path d="M6 0a6 6 0 0 0-6 6c0 4.5 6 10 6 10s6-5.5 6-10a6 6 0 0 0-6-6zm0 8.5A2.5 2.5 0 1 1 6 3.5a2.5 2.5 0 0 1 0 5z" fill="#fff"/></svg><span>Lorem Ipsum is simply dummy text of the<br>printing and typesetting industry.</span></li>
    <li><svg width="14" height="14" viewBox="0 0 24 24"><path d="M6.6 10.8a15.2 15.2 0 0 0 6.6 6.6l2.2-2.2a1 1 0 0 1 1-.25 11.4 11.4 0 0 0 3.6.57 1 1 0 0 1 1 1V20a1 1 0 0 1-1 1A17 17 0 0 1 3 4a1 1 0 0 1 1-1h3.5a1 1 0 0 1 1 1c0 1.25.2 2.45.57 3.57a1 1 0 0 1-.25 1z" fill="#fff"/></svg><span>555.210.4417</span></li>
    <li><svg width="14" height="14" viewBox="0 0 24 24"><path d="M6.6 10.8a15.2 15.2 0 0 0 6.6 6.6l2.2-2.2a1 1 0 0 1 1-.25 11.4 11.4 0 0 0 3.6.57 1 1 0 0 1 1 1V20a1 1 0 0 1-1 1A17 17 0 0 1 3 4a1 1 0 0 1 1-1h3.5a1 1 0 0 1 1 1c0 1.25.2 2.45.57 3.57a1 1 0 0 1-.25 1z" fill="#fff"/></svg><span>555.210.4482</span></li>
    <li><svg width="14" height="12" viewBox="0 0 14 12"><rect x="0" y="0" width="14" height="12" rx="1" fill="#fff"/><path d="M1 1l6 5 6-5" fill="none" stroke="#050505" stroke-width="1.5"/></svg><span>info@qbpane.example</span></li>
  </ul>
  <div class="abs" style="left:1024px;top:50px"><div class="footer-head">Quick Links</div></div>
  <ul class="abs links" style="top:94px">
    <li>Home</li><li>About Us</li><li>Services</li><li>News</li><li>Testimonial</li><li>Contact Us</li>
  </ul>
</footer>

</body>
</html>
```